I need a business card to give to prospective clients. I am a freelance photographer who photographs most things (except weddings and social stuff) including nature, wildlife and interiors.
I want to look modern and stylish.
I am including a photograph although I am by no means certain that it should be used - what do you think?
More of my images can be seen and downloaded at my Lensora page - just search for Marla Vintree
Target Market(s)
Home owners selling or letting properties, private individuals wanting to buy prints
Industry/Entity Type
Business
Contact Information for Business Card
Marla Vintree Photography
Marla
Fenwick Lodge, Copper Mill Road, Ashbrook, Wrenfield, IP31 4QT
Tel: +44 7700 418263. Email: marla@marlavintree.co.uk

```html
<!DOCTYPE html>
<html lang="en">
<head>
<meta charset="utf-8">
<title>Marla Vintree Photography – Business Card</title>
<link rel="stylesheet" href="https://fonts.googleapis.com/css2?family=Cinzel:wght@400&family=Open+Sans:wght@400;700&display=swap">
<style>
  :root {
    --page-bg: #1f1f1f;
    --card-back-bg: #2b2829;
    --card-back-text: #cbc7c7;
    --accent-green: #2e9e45;
    --text-white: #ffffff;
    --text-light: #e6e6e6;
    --text-muted: #cfcfcf;
    --photo-light: #d4d4d4;
    --photo-mid: #9a9a9a;
    --photo-dark: #1c1c1c;
  }
  * { box-sizing: border-box; margin: 0; padding: 0; }
  html, body {
    width: 1200px; height: 900px; overflow: hidden;
    background: var(--page-bg);
  }
  .canvas {
    width: 1200px; height: 900px;
    display: flex; flex-direction: column;
    align-items: center; justify-content: center; gap: 40px;
  }
  .card {
    position: relative;
    width: 700px; height: 400px;
    overflow: hidden;
    box-shadow: 0 10px 30px rgba(0,0,0,.5);
  }

  /* Back side */
  .card-back { background: var(--card-back-bg); }
  .card-back__headline {
    position: absolute; left: 64px; top: 150px;
    font-family: "Cinzel", serif;
    font-weight: 400; font-size: 52px; line-height: 1.15;
    color: var(--card-back-text);
    letter-spacing: 1px;
  }

  /* Front side */
  .card-front__photo {
    position: absolute; inset: 0;
    background:
      linear-gradient(180deg, rgba(0,0,0,0) 40%, rgba(20,20,20,.85) 78%, var(--photo-dark) 100%),
      linear-gradient(90deg, var(--photo-light) 0%, var(--photo-mid) 30%, #bdbdbd 45%, #7c7c7c 60%, var(--photo-light) 80%, #a5a5a5 100%);
  }
  .brand {
    position: absolute; left: 60px; top: 56px;
    font-family: "Open Sans", sans-serif;
    font-weight: 700; font-size: 30px; letter-spacing: .3px;
    color: var(--text-white);
    text-transform: uppercase;
  }

  .services {
    position: absolute; left: 200px; top: 214px;
    display: flex; align-items: center; gap: 10px;
    font-family: "Open Sans", sans-serif;
    font-weight: 700; font-size: 24px;
    color: var(--text-light); text-transform: uppercase;
  }
  .services__divider {
    width: 3px; height: 22px; background: var(--accent-green);
  }

  .contact {
    position: absolute;
    font-family: "Open Sans", sans-serif;
    font-weight: 400; font-size: 18px;
    color: var(--text-muted);
    display: flex; align-items: center; gap: 10px;
    white-space: nowrap;
  }
  .contact svg { width: 20px; height: 20px; fill: var(--text-muted); flex: none; }
  .contact--phone { left: 176px; top: 268px; }
  .contact--email { left: 410px; top: 268px; }
  .contact--address { left: 176px; top: 312px; }
  .contact__address-line2 {
    position: absolute; left: 420px; top: 344px;
    font-family: "Open Sans", sans-serif; font-size: 18px; color: var(--text-muted);
  }
</style>
</head>
<body>
<main class="canvas">

  <section class="card card-back">
    <h2 class="card-back__headline">Looking for a<br>Photographer ?</h2>
  </section>

  <section class="card card-front">
    <div class="card-front__photo" role="img" aria-label="Black and white photograph of an elephant's legs with one foot raised"></div>

    <h1 class="brand">Marla Vintree Photography</h1>

    <p class="services">
      <span>Nature</span><span class="services__divider"></span>
      <span>Wildlife</span><span class="services__divider"></span>
      <span>Interiors</span>
    </p>

    <p class="contact contact--phone">
      <svg viewBox="0 0 24 24" aria-hidden="true"><path d="M6.6 10.8a15.1 15.1 0 0 0 6.6 6.6l2.2-2.2a1 1 0 0 1 1-.25 11.4 11.4 0 0 0 3.6.57 1 1 0 0 1 1 1V20a1 1 0 0 1-1 1A17 17 0 0 1 3 4a1 1 0 0 1 1-1h3.5a1 1 0 0 1 1 1c0 1.25.2 2.46.57 3.6a1 1 0 0 1-.25 1z"/></svg>
      +44 7700 418263
    </p>
    <p class="contact contact--email">
      <svg viewBox="0 0 24 24" aria-hidden="true"><path d="M2 5h20v14H2z M4 7v.4l8 5.2 8-5.2V7z" fill-rule="evenodd"/></svg>
      marla@marlavintree.co.uk
    </p>
    <p class="contact contact--address">
      <svg viewBox="0 0 24 24" aria-hidden="true"><path d="M12 3 2 12h3v8h5v-6h4v6h5v-8h3z"/></svg>
      Marla Fenwick Lodge, Copper Mill Road, Ashbrook,
    </p>
    <p class="contact__address-line2">Wrenfield, IP31 4QT</p>
  </section>

</main>
</body>
</html>
```